Stationary set for consulting company
Tarvo Bridge
Creative Brief
Modern
Karim Yusuf Al Banna
Co-Founder
Reef Spire, Abu Dhabi United Arab Emirates
karim@tarvobridge.ae
www.tarvobridge.com
I need a full stationary set for the company logo I will be attaching. (PPTs, business cards, envelope, letterhead, etc)

```html
<!DOCTYPE html>
<html lang="en">
<head>
<meta charset="utf-8">
<title>Tarvo Bridge Consulting – Stationery Set</title>
<link href="https://fonts.googleapis.com/css2?family=Montserrat:wght@400;500;600;700&display=swap" rel="stylesheet">
<style>
:root{
  --navy:#233b82;
  --navy-deep:#1c3170;
  --sky:#a8c4ea;
  --paper:#ffffff;
  --ink:#3a3f4a;
  --muted:#8a8f99;
  --backdrop:#e9e5df;
}
*{box-sizing:border-box;margin:0;padding:0}
html,body{width:1200px;height:502px;overflow:hidden}
body{background:var(--backdrop);font-family:"Montserrat",sans-serif;position:relative}
.piece{position:absolute;box-shadow:0 2px 6px rgba(0,0,0,.18)}
.brand{color:var(--paper);font-weight:700;text-transform:uppercase;letter-spacing:.06em;display:flex;align-items:center;gap:6px;line-height:1}
.brand-mark{width:10px;height:10px;background:var(--paper);flex:none}
.brand-sub{font-weight:500;font-size:7px;letter-spacing:.3em;color:var(--paper);margin-top:3px}

/* business card front */
.card-front{left:36px;top:36px;width:463px;height:211px;background:var(--navy);overflow:hidden}
.card-front .logo{position:absolute;left:22px;top:22px}
.card-front .brand{font-size:16px}
.card-front .brand-sub{margin-left:16px}
.card-front .holder{position:absolute;left:22px;top:118px;color:var(--paper)}
.holder-name{font-weight:600;font-size:13px;text-transform:uppercase;letter-spacing:.03em}
.holder-title{font-size:11px;margin-top:3px}
.card-front .divider{position:absolute;left:228px;top:90px;width:1px;height:92px;background:var(--paper)}
.contacts{position:absolute;left:242px;top:92px;list-style:none;color:var(--paper);font-size:9.5px}
.contacts li{display:flex;align-items:flex-start;gap:8px;margin-bottom:6px;line-height:1.25}
.contacts svg{width:10px;height:10px;flex:none;margin-top:1px}
.card-stripe{position:absolute;left:0;right:0;bottom:0;height:10px;background:var(--sky)}

/* business card back */
.card-back{left:36px;top:283px;width:463px;height:209px;background:var(--navy)}
.card-back .brand{position:absolute;left:40px;top:84px;font-size:30px;gap:12px}
.card-back .brand-mark{width:22px;height:22px}

/* letterhead */
.letterhead{left:509px;top:36px;width:302px;height:456px;background:var(--paper);overflow:hidden}
.letter-band{height:52px;background:var(--navy);display:flex;flex-direction:column;align-items:center;justify-content:center}
.letter-band .brand{font-size:11px}
.letter-band .brand-sub{font-size:5px}
.letter-body{padding:14px 22px 0;color:var(--ink);font-size:4.6px;line-height:1.75}
.letter-body p{margin-bottom:8px}
.signature{width:46px;height:14px;margin:10px 0 4px;background:linear-gradient(90deg,#c9ccd3,#eceef1)}
.letter-foot{position:absolute;left:0;right:0;bottom:12px;display:flex;justify-content:space-between;padding:0 14px;font-size:4px;color:var(--muted);border-top:.5px solid #dde0e5;padding-top:5px}
.letter-base{position:absolute;left:0;right:0;bottom:0;height:6px;background:var(--navy)}

/* envelope front */
.envelope-front{left:828px;top:36px;width:343px;height:187px;background:var(--navy);overflow:hidden}
.envelope-front .brand{position:absolute;left:22px;top:22px;font-size:14px}
.envelope-front .brand-sub{margin-left:16px;font-size:6px}
.envelope-front .address{position:absolute;right:22px;top:24px;text-align:right;color:var(--paper);font-size:6.5px;line-height:1.6}

/* envelope back */
.envelope-back{left:828px;top:271px;width:343px;height:185px;background:var(--navy);overflow:hidden}
.envelope-back svg{position:absolute;inset:0}
</style>
</head>
<body>

<section class="piece card-front" aria-label="Business card front">
  <div class="logo">
    <div class="brand"><span class="brand-mark"></span>Tarvo Bridge</div>
    <div class="brand-sub">CONSULTING</div>
  </div>
  <div class="holder">
    <div class="holder-name">Karim Yusuf Al Banna</div>
    <div class="holder-title">Co-Founder</div>
  </div>
  <div class="divider"></div>
  <ul class="contacts">
    <li><svg viewBox="0 0 10 10"><path d="M2 1l2 0 1 2-1 1c.5 1 1 1.5 2 2l1-1 2 1 0 2c-4 .5-7.5-3-7-7z" fill="#fff"/></svg>+971-50-4418203</li>
    <li><svg viewBox="0 0 10 10"><rect x="1" y="2" width="8" height="6" fill="none" stroke="#fff"/><path d="M1 2l4 3 4-3" fill="none" stroke="#fff"/></svg>karim@tarvobridge.ae</li>
    <li><svg viewBox="0 0 10 10"><circle cx="5" cy="5" r="4" fill="none" stroke="#fff"/><path d="M1 5h8M5 1v8" stroke="#fff" stroke-width=".7"/></svg>www.tarvobridge.com</li>
    <li><svg viewBox="0 0 10 10"><path d="M5 9S2 5.5 2 4a3 3 0 016 0c0 1.5-3 5-3 5z" fill="#fff"/></svg>Reef Spire, Abu Dhabi<br>United Arab Emirates</li>
  </ul>
  <div class="card-stripe"></div>
</section>

<section class="piece card-back" aria-label="Business card back">
  <div class="brand"><span class="brand-mark"></span>Tarvo Bridge</div>
</section>

<section class="piece letterhead" aria-label="Letterhead">
  <header class="letter-band">
    <div class="brand"><span class="brand-mark" style="width:7px;height:7px"></span>Tarvo Bridge</div>
    <div class="brand-sub">CONSULTING</div>
  </header>
  <div class="letter-body">
    <p>Dear Mr. Haddad,</p>
    <p>Thank you for meeting with our team last week. We are pleased to share a summary of the advisory plan we discussed, covering strategy, operations and regional growth for the coming year.</p>
    <p>Our consultants will work closely with your managers to review current processes, identify clear priorities and set measurable goals. Each stage will be reported in writing so progress stays visible.</p>
    <p>Please review the attached proposal and let us know if any changes are needed. We look forward to a long and useful partnership.</p>
    <div class="signature" role="img" aria-label="Handwritten signature"></div>
    <p>Sincerely,</p>
  </div>
  <footer class="letter-foot">
    <span>+971-50-4418203</span>
    <span>karim@tarvobridge.ae</span>
    <span>www.tarvobridge.com</span>
    <span>Reef Spire, Abu Dhabi</span>
  </footer>
  <div class="letter-base"></div>
</section>

<section class="piece envelope-front" aria-label="Envelope front">
  <div class="brand"><span class="brand-mark"></span>Tarvo Bridge</div>
  <div class="brand-sub" style="position:absolute;left:22px;top:39px;margin-left:16px">CONSULTING</div>
  <div class="address">Reef Spire, Abu Dhabi<br>United Arab Emirates<br>www.tarvobridge.com</div>
  <div class="card-stripe"></div>
</section>

<section class="piece envelope-back" aria-label="Envelope back">
  <svg viewBox="0 0 343 185" preserveAspectRatio="none">
    <path d="M0 0L171.5 95 343 0" fill="none" stroke="#3a52a0" stroke-width="1.2"/>
    <path d="M0 185L150 92M343 185L193 92" fill="none" stroke="#2d4690" stroke-width="1"/>
    <rect x="0" y="175" width="343" height="10" fill="var(--sky)"/>
  </svg>
</section>

</body>
</html>
```